Tolvern Business Cards

Business card design. dont mind if new logo is suggested.
it would be for a security company.
our clients would be bigger security companies around Australia.
have a logo done but can be replaced. see attaached. like the colors.
Need company name, person name, designation, phone and email on front.
At back company logo and name. website saddress and 2 x license numbers
would like to have 2 different background color for both sidde

Industry/Entity Type

Security

Contact Information for Business Card

round corners, front should be light in color. need logo at back with webaddress and 2 x license numners

Font styles to use
Sans Serif

Colors
f37122
faa54b
f8ba93
0255a3
0592cd
85cae6
b3d448
9bcb3c
ffffff

Requirements
Must have
• see description
Nice to have
• see description
Should not have
• should not be difficult to read or hardd to find information on card.. lets say easy on eyes yet catchy

```html
<!DOCTYPE html>
<html lang="en">
<head>
<meta charset="utf-8">
<title>Tolvern Security Group – Business Cards</title>
<link rel="stylesheet" href="https://fonts.googleapis.com/css2?family=Open+Sans:wght@400;700&display=swap">
<style>
  :root {
    --canvas-bg: #e4e5e7;
    --card-white: #ffffff;
    --navy: #1b2a6b;
    --ink: #3a3d44;
    --muted: #5c6069;
    --rule: #2f4a8a;
    --teal-light: #0d9cc4;
    --teal-mid: #137fb0;
    --teal-deep: #1a5a8e;
    --bubble-cyan: #bff3f7;
    --bubble-lilac: #d5d9ef;
    --mark-blue: #0592cd;
    --back-text: rgba(255,255,255,0.88);
  }
  * { box-sizing: border-box; margin: 0; padding: 0; }
  html, body {
    width: 1200px; height: 1200px; overflow: hidden;
    background: var(--canvas-bg);
    font-family: "Open Sans", Arial, sans-serif;
  }
  .sheet {
    width: 1200px; height: 1200px;
    display: flex; flex-direction: column; align-items: center; justify-content: center;
    gap: 60px;
  }
  .card {
    position: relative;
    width: 860px; height: 491px;
    border-radius: 18px;
    overflow: hidden;
    box-shadow: 0 10px 28px rgba(0,0,0,0.12);
  }

  /* Front */
  .card-front { background: var(--card-white); }
  .front-bubbles {
    position: absolute; right: 0; top: 0; width: 360px; height: 100%;
    background:
      radial-gradient(circle at 45% 28%, var(--bubble-cyan) 0, rgba(191,243,247,0) 40%),
      radial-gradient(circle at 78% 62%, var(--bubble-lilac) 0, rgba(213,217,239,0) 42%),
      radial-gradient(circle at 40% 82%, var(--bubble-cyan) 0, rgba(191,243,247,0) 34%);
    -webkit-mask-image: linear-gradient(to right, transparent 0%, #000 45%);
    mask-image: linear-gradient(to right, transparent 0%, #000 45%);
  }
  .brand {
    position: absolute; left: 200px; top: 48px;
    display: flex; align-items: center; gap: 14px;
  }
  .brand-dot {
    width: 40px; height: 40px; border-radius: 50%;
    background: var(--mark-blue);
  }
  .brand-name {
    font-size: 22px; font-weight: 700; letter-spacing: 1px;
    color: var(--navy); white-space: nowrap;
  }
  .person { position: absolute; left: 60px; top: 135px; }
  .person-name {
    font-size: 34px; font-weight: 700; color: var(--navy); letter-spacing: -0.5px;
    line-height: 1.1;
  }
  .person-role { font-size: 19px; color: var(--muted); margin-top: 2px; }
  .rule {
    position: absolute; left: 250px; right: 0; top: 236px;
    height: 1px; background: var(--rule);
  }
  .contact {
    position: absolute; left: 60px; top: 262px;
    font-size: 18px; color: var(--ink); line-height: 1.55;
  }
  .divider {
    position: absolute; left: 395px; top: 300px;
    width: 1px; height: 52px; background: var(--muted);
  }
  .address {
    position: absolute; left: 415px; top: 298px;
    font-size: 18px; color: var(--ink); line-height: 1.55;
  }

  /* Back */
  .card-back {
    background: linear-gradient(135deg, var(--teal-light) 0%, var(--teal-mid) 45%, var(--teal-deep) 100%);
  }
  .back-bubbles {
    position: absolute; right: 0; top: 0; width: 600px; height: 100%;
    background:
      radial-gradient(ellipse at 50% 55%, rgba(20,70,120,0.35) 0, rgba(20,70,120,0) 60%);
  }
  .back-brand {
    position: absolute; left: 70px; top: 180px;
    display: flex; align-items: center; gap: 16px;
  }
  .back-brand .brand-dot { background: var(--card-white); width: 46px; height: 46px; }
  .back-brand .brand-name { color: var(--card-white); font-size: 26px; }
  .back-details {
    position: absolute; left: 70px; top: 260px;
    font-size: 17px; line-height: 1.6; color: var(--back-text);
  }
  .back-web { font-weight: 700; color: var(--card-white); margin-bottom: 6px; }
</style>
</head>
<body>
<main class="sheet">
  <section class="card card-front" aria-label="Business card front">
    <div class="front-bubbles" role="img" aria-label="Decorative pattern of soft cyan and lilac circles"></div>
    <div class="brand">
      <span class="brand-dot"></span>
      <span class="brand-name">TOLVERN SECURITY GROUP</span>
    </div>
    <div class="person">
      <p class="person-name">ALEX MARSH</p>
      <p class="person-role">Director</p>
    </div>
    <div class="rule"></div>
    <div class="contact">
      <p>1-555-010-2030</p>
      <p>www.tolvernsecurity.com</p>
      <p>alex@tolvernsecurity.com</p>
    </div>
    <div class="divider"></div>
    <div class="address">
      <p>Dummy city</p>
      <p>Dummy Country Land</p>
    </div>
  </section>

  <section class="card card-back" aria-label="Business card back">
    <div class="back-bubbles" role="img" aria-label="Faint decorative pattern of darker blue circles"></div>
    <div class="back-brand">
      <span class="brand-dot"></span>
      <span class="brand-name">TOLVERN SECURITY GROUP</span>
    </div>
    <div class="back-details">
      <p class="back-web">www.tolvernsecurity.com</p>
      <p>Licence No. 000-111-222</p>
      <p>Licence No. 000-333-444</p>
    </div>
  </section>
</main>
</body>
</html>
```